Single brochure for international companies in the financial sector

We need to update a brochure 4 pages presenting our company. We are a financial engineering company. The final design must provide financial security, service and trust. you will find the current brochure copy. Our color code is Orange (RGB 235/100/68), Black, White and Gray. photos show the visual of the site, but it is not mandatory to keep them.

Target Market(s)

wealth management professionals

Industry/Entity Type

Finance

Requirements
Must have
• Logo Tolvane Capital all text in the document color Orange Tolvane (RGB 235/100/68)
Nice to have
• Vista Font
Should not have
• images / pictures of people

```html
<!DOCTYPE html>
<html lang="en">
<head>
<meta charset="utf-8">
<title>Tolvane Capital – Brochure</title>
<link rel="stylesheet" href="https://fonts.googleapis.com/css2?family=Fira+Sans:wght@400;500;600&family=Fira+Sans+Condensed:wght@600;700&display=swap">
<style>
  :root {
    --orange: #eb6444;
    --orange-deep: #e2432a;
    --orange-soft: #f3a48e;
    --gray: #6d6d6d;
    --text-gray: #555555;
    --backdrop: #58565a;
    --white: #ffffff;
  }
  html, body {
    margin: 0;
    padding: 0;
    width: 1200px;
    height: 1200px;
    overflow: hidden;
    background: var(--backdrop);
    font-family: "Fira Sans", Arial, sans-serif;
  }
  .spread {
    position: absolute;
    left: 244px;
    top: 93px;
    width: 714px;
    height: 1016px;
  }
  .page {
    position: absolute;
    width: 356px;
    height: 502px;
    background: var(--white);
    overflow: hidden;
  }
  .page--back { left: 0; top: 0; }
  .page--cover { left: 358px; top: 0; }
  .page--company { left: 0; top: 514px; }
  .page--services { left: 358px; top: 514px; }
  .page svg.page-art {
    position: absolute;
    inset: 0;
    width: 100%;
    height: 100%;
  }

  /* Back cover */
  .legal {
    position: absolute;
    left: 52px;
    top: 191px;
    width: 250px;
    margin: 0;
    color: var(--white);
    font-size: 13px;
    line-height: 17.5px;
    text-align: center;
  }
  .legal .web { display: block; margin-top: 17px; }

  /* Cover */
  .brand-card {
    position: absolute;
    left: 83px;
    top: 74px;
    width: 186px;
    height: 96px;
    background: var(--white);
    box-shadow: 0 2px 6px rgba(0,0,0,0.25);
    display: flex;
    flex-direction: column;
    align-items: center;
    justify-content: center;
  }
  .brand-card .brand-name {
    margin: 0;
    font-size: 15px;
    font-weight: 400;
    color: #222222;
    letter-spacing: 0.42em;
    line-height: 23px;
    text-align: center;
    padding-left: 0.42em;
  }
  .tagline {
    position: absolute;
    left: 0;
    width: 356px;
    top: 456px;
    margin: 0;
    text-align: center;
    color: var(--orange);
    font-weight: 600;
    font-size: 18px;
  }

  /* Inner pages */
  .page-title {
    position: absolute;
    left: 0;
    top: 1px;
    width: 232px;
    height: 52px;
    background: var(--orange);
    clip-path: polygon(0 0, 100% 0, 93% 100%, 0 100%);
    margin: 0;
    color: var(--white);
    font-family: "Fira Sans Condensed", "Arial Narrow", sans-serif;
    font-weight: 700;
    font-size: 27px;
    line-height: 52px;
    padding-left: 18px;
    box-sizing: border-box;
  }
  .page--services .page-title { padding-left: 13px; }
  .section {
    position: absolute;
    left: 25px;
  }
  .page--services .section { left: 24px; }
  .section h3 {
    margin: 0 0 7px;
    color: var(--orange);
    font-weight: 400;
    font-size: 21px;
    line-height: 26px;
  }
  .section p {
    margin: 0 0 0 18px;
    width: 225px;
    color: var(--text-gray);
    font-size: 10.5px;
    line-height: 13.2px;
  }
  .page--services .section p { margin-left: 23px; width: 250px; }
  .s1 { top: 84px; }
  .s2 { top: 223px; }
  .s3 { top: 362px; }
</style>
</head>
<body>
<main class="spread">

  <section class="page page--back" aria-label="Back cover">
    <svg class="page-art" viewBox="0 0 420 593" preserveAspectRatio="none" aria-hidden="true">
      <path d="M0 205 C 60 85, 190 12, 345 0" fill="none" stroke="var(--gray)" stroke-width="9"/>
      <path d="M352 0 L420 0 L420 240 C 400 450, 260 570, 110 593 L0 593 L0 222 C 60 88, 200 12, 352 0 Z" fill="var(--orange)"/>
      <path d="M420 275 C 395 470, 270 575, 150 593" fill="none" stroke="var(--gray)" stroke-width="9"/>
    </svg>
    <p class="legal">Tolvane Capital SA. Capital : 000 400<br>Euros<br>RCS Paris&nbsp; : 512 418 063<br>Code Banque (CIB) : 14872<span class="web">www.tolvanecapital.com</span></p>
  </section>

  <section class="page page--cover" aria-label="Front cover">
    <svg class="page-art" viewBox="0 0 420 593" preserveAspectRatio="none">
      <defs>
        <radialGradient id="petal-glow" cx="0.8" cy="0.62" r="0.75">
          <stop offset="0" stop-color="var(--orange-deep)"/>
          <stop offset="0.55" stop-color="#ec7a61"/>
          <stop offset="1" stop-color="var(--orange-soft)"/>
        </radialGradient>
      </defs>
      <path role="img" aria-label="Abstract illustration of soft orange petals"
            d="M0 68 C 60 110, 130 130, 210 130 C 300 130, 370 115, 420 88 L420 500 C 360 445, 260 418, 180 420 C 100 424, 40 448, 0 468 Z"
            fill="url(#petal-glow)"/>
      <path d="M0 72 C 40 100, 80 118, 110 126" fill="none" stroke="var(--orange-deep)" stroke-width="7"/>
      <path d="M300 150 C 350 142, 390 130, 420 113" fill="none" stroke="var(--white)" stroke-width="6"/>
      <path d="M0 470 C 90 425, 220 410, 330 425 L420 460 L420 500 C 360 445, 260 420, 180 422 C 100 426, 40 450, 0 480 Z" fill="var(--white)"/>
      <path d="M0 545 C 70 470, 230 440, 405 500 C 300 462, 120 468, 0 518 Z" fill="var(--gray)"/>
    </svg>
    <div class="brand-card">
      <p class="brand-name">TOLVANE<br>CAPITAL</p>
    </div>
    <p class="tagline">Financial Engineering</p>
  </section>

  <section class="page page--company" aria-label="The Company">
    <h2 class="page-title">The Company</h2>
    <article class="section s1">
      <h3>about us</h3>
      <p>Tolvane Capital is a financial engineering company.<br>It is fully independent from any bank or any other company.</p>
    </article>
    <article class="section s2">
      <h3>our clients</h3>
      <p>Our clients are financial professionals such as asset managers, institutionnals, corporates, private banks, wealth managers and family offices.<br>Our purpose is to make their work easier, every day.</p>
    </article>
    <article class="section s3">
      <h3>what we do</h3>
      <p>We provide them with investment solutions designed to improve their portfolios performance.<br>Simple as that.</p>
    </article>
  </section>

  <section class="page page--services" aria-label="Our Services">
    <h2 class="page-title">Our Services</h2>
    <article class="section s1">
      <h3>portfolio analysis</h3>
      <p>We advise our clients on their portfolios of financial products. Together we identify the needs for restructuring or reallocating the assets.<br>We also provide full monitoring and reporting services throughout the life of the products.</p>
    </article>
    <article class="section s2">
      <h3>partner selection</h3>
      <p>Our internal tools allow us to continuously assess the issuers we are working with.<br>Therefore we give our clients the luxury to chose among the best issuers for their investment solution.</p>
    </article>
    <article class="section s3">
      <h3>investment advice</h3>
      <p>Each client is looking for a unique investment solution. Hence, we combine internal and external resources to create the financial product that will best fit our clients requirements.<br>Thanks to a truly independent advice, we offer bespoke, simple and efficient solutions.</p>
    </article>
  </section>

</main>
</body>
</html>
```